Poster of Core Values & Motto

Create our core values poster and motto. Attached are our core values and our Motto. This poster represents both of our companies Tidy Pulp & CuraBinix.

Target Market(s)

Our team / employees

Industry/Entity Type

Shredding and Medical Waste

Colors
59FF00
82FF00
B8FF75
E3FFCB
F4FFEA
EB3D1F
EC4F4E
F09395
F8D3D4
FCEDEE

Requirements
Must have
• Include both companies logos

```html
<!DOCTYPE html>
<html lang="en">
<head>
<meta charset="utf-8">
<title>Core Values Poster – Tidy Pulp &amp; CuraBinix</title>
<link rel="stylesheet" href="https://fonts.googleapis.com/css2?family=Montserrat:wght@400;800;900&display=swap">
<style>
  :root {
    --backdrop: #263238;
    --paper: #ffffff;
    --ink: #231f20;
    --title-red: #d42228;
    --team-green: #0d6630;
    --excellence-blue: #1a9fc6;
    --honesty-red: #f80c0f;
    --dependable-orange: #f56613;
    --secure-magenta: #b8135f;
    --efficient-yellow: #f5bf10;
    --brand-green: #1e8a3c;
  }
  html, body {
    margin: 0;
    padding: 0;
    width: 988px;
    height: 1200px;
    overflow: hidden;
    background: var(--backdrop);
  }
  .poster-canvas {
    display: block;
    width: 988px;
    height: 1200px;
    font-family: "Montserrat", sans-serif;
  }
  .sheet { fill: var(--paper); }
  .title-band { fill: var(--title-red); }
  .title-core { fill: var(--title-red); font-weight: 900; font-size: 140px; }
  .title-values { fill: var(--paper); font-weight: 900; font-size: 228px; }
  .value-heading { fill: var(--paper); font-weight: 900; font-size: 42px; }
  .value-body { fill: var(--paper); font-weight: 400; font-size: 24px; }
  .value-heading.dark { fill: var(--ink); }
  .value-body.dark { fill: var(--ink); }
  .seg-green { fill: var(--team-green); }
  .seg-blue { fill: var(--excellence-blue); }
  .seg-red { fill: var(--honesty-red); }
  .seg-orange { fill: var(--dependable-orange); }
  .seg-magenta { fill: var(--secure-magenta); }
  .seg-yellow { fill: var(--efficient-yellow); }
  .icon-spot { fill: #000000; opacity: 0.12; }
  .motto-label { fill: var(--ink); font-weight: 800; font-size: 19px; letter-spacing: 4px; }
  .motto-rule { stroke: var(--ink); stroke-width: 2; stroke-dasharray: 6 5; }
  .motto-line { fill: var(--ink); font-weight: 900; }
  .brand-name { fill: var(--ink); font-weight: 900; font-size: 44px; }
  .brand-dot { fill: var(--brand-green); }
</style>
</head>
<body>
<svg class="poster-canvas" viewBox="0 0 1736 2109" xmlns="http://www.w3.org/2000/svg" xmlns:xlink="http://www.w3.org/1999/xlink">
  <defs>
    <path id="value-segment" d="M445.7,-235.4 A504,504 0 0 1 445.7,235.4 L232.3,112.2 A258,258 0 0 0 256.1,31.4 L200,0 L256.1,-31.4 A258,258 0 0 0 232.3,-112.2 Z"/>
  </defs>

  <rect class="sheet" x="316" y="225" width="1106" height="1660"/>

  <!-- Heading -->
  <g class="poster-title">
    <path class="title-band" d="M453,328 H528 L645,432 H1090 L1207,328 H1285 A45,45 0 0 1 1330,373 V599 A45,45 0 0 1 1285,644 H453 A45,45 0 0 1 408,599 V373 A45,45 0 0 1 453,328 Z"/>
    <text class="title-core" x="655" y="420" textLength="430" lengthAdjust="spacing">CORE</text>
    <text class="title-values" x="466" y="615" textLength="810" lengthAdjust="spacingAndGlyphs">VALUES</text>
  </g>

  <!-- Values wheel -->
  <g class="values-wheel" transform="translate(868 1277)">
    <use xlink:href="#value-segment" class="seg-red"/>
    <use xlink:href="#value-segment" class="seg-orange" transform="rotate(60)"/>
    <use xlink:href="#value-segment" class="seg-magenta" transform="rotate(120)"/>
    <use xlink:href="#value-segment" class="seg-yellow" transform="rotate(180)"/>
    <use xlink:href="#value-segment" class="seg-green" transform="rotate(240)"/>
    <use xlink:href="#value-segment" class="seg-blue" transform="rotate(300)"/>
  </g>

  <!-- Value icons -->
  <g role="img" aria-label="Line icon of two hands clasped in a handshake"><circle class="icon-spot" cx="760" cy="880" r="62"/></g>
  <g role="img" aria-label="Line icon of a cheering person rising from a box"><circle class="icon-spot" cx="975" cy="875" r="62"/></g>
  <g role="img" aria-label="Line icon of a raised hand beside a heart"><circle class="icon-spot" cx="1262" cy="1180" r="62"/></g>
  <g role="img" aria-label="Line icon of a clock inside a gear"><circle class="icon-spot" cx="489" cy="1188" r="62"/></g>
  <g role="img" aria-label="Line icon of a hand holding a shield with a tick"><circle class="icon-spot" cx="582" cy="1555" r="62"/></g>
  <g role="img" aria-label="Line icon of a person working at a laptop"><circle class="icon-spot" cx="1087" cy="1525" r="62"/></g>

  <!-- Value texts -->
  <g class="value synergy">
    <text class="value-heading" x="537" y="960" textLength="213" lengthAdjust="spacingAndGlyphs">SYNERGY /</text>
    <text class="value-heading" x="537" y="997" textLength="248" lengthAdjust="spacingAndGlyphs">TEAMWORK</text>
    <text class="value-body" x="537" y="1022" textLength="271" lengthAdjust="spacingAndGlyphs">Get it done attitude with</text>
    <text class="value-body" x="537" y="1048" textLength="212" lengthAdjust="spacingAndGlyphs">humble confidence</text>
  </g>
  <g class="value excellence">
    <text class="value-heading" x="946" y="970" textLength="254" lengthAdjust="spacingAndGlyphs">EXCELLENCE</text>
    <text class="value-body" x="946" y="996" textLength="231" lengthAdjust="spacingAndGlyphs">Exceed expectations</text>
    <text class="value-body" x="946" y="1022" textLength="128" lengthAdjust="spacingAndGlyphs">with a smile</text>
  </g>
  <g class="value honesty">
    <text class="value-heading" x="1152" y="1285" textLength="190" lengthAdjust="spacingAndGlyphs">HONESTY</text>
    <text class="value-heading" x="1143" y="1323" textLength="208" lengthAdjust="spacingAndGlyphs">INTEGRITY</text>
    <text class="value-body" x="1151" y="1350" textLength="191" lengthAdjust="spacingAndGlyphs">Do the right thing</text>
  </g>
  <g class="value efficient">
    <text class="value-heading dark" x="395" y="1310" textLength="196" lengthAdjust="spacingAndGlyphs">EFFICIENT</text>
    <text class="value-body dark" x="397" y="1336" textLength="191" lengthAdjust="spacingAndGlyphs">on-time, sense of</text>
    <text class="value-body dark" x="404" y="1361" textLength="176" lengthAdjust="spacingAndGlyphs">urgency, always</text>
    <text class="value-body dark" x="399" y="1387" textLength="187" lengthAdjust="spacingAndGlyphs">trying to improve</text>
  </g>
  <g class="value secure">
    <text class="value-heading" x="624" y="1590" textLength="204" lengthAdjust="spacingAndGlyphs">SAFE AND</text>
    <text class="value-heading" x="671" y="1628" textLength="157" lengthAdjust="spacingAndGlyphs">SECURE</text>
    <text class="value-body" x="597" y="1655" textLength="231" lengthAdjust="spacingAndGlyphs">we are just as secure</text>
    <text class="value-body" x="609" y="1681" textLength="219" lengthAdjust="spacingAndGlyphs">as an armored truck</text>
    <text class="value-body" x="701" y="1707" textLength="127" lengthAdjust="spacingAndGlyphs">with money</text>
  </g>
  <g class="value dependable">
    <text class="value-heading" x="925" y="1645" textLength="257" lengthAdjust="spacingAndGlyphs">DEPENDABLE</text>
    <text class="value-body" x="925" y="1672" textLength="180" lengthAdjust="spacingAndGlyphs">Do what you say</text>
    <text class="value-body" x="925" y="1698" textLength="118" lengthAdjust="spacingAndGlyphs">you will do</text>
  </g>

  <!-- Motto -->
  <g class="motto" text-anchor="middle">
    <line class="motto-rule" x1="706" y1="1181" x2="820" y2="1181"/>
    <line class="motto-rule" x1="918" y1="1181" x2="1030" y2="1181"/>
    <text class="motto-label" x="870" y="1188">MOTTO</text>
    <text class="motto-line" x="868" y="1232" font-size="38" textLength="298" lengthAdjust="spacingAndGlyphs">REMIND PEOPLE</text>
    <text class="motto-line" x="868" y="1280" font-size="58" textLength="358" lengthAdjust="spacingAndGlyphs">WHAT GREAT</text>
    <text class="motto-line" x="863" y="1345" font-size="82" textLength="331" lengthAdjust="spacingAndGlyphs">SERVICE</text>
    <text class="motto-line" x="868" y="1382" font-size="38" textLength="215" lengthAdjust="spacingAndGlyphs">LOOKS LIKE</text>
  </g>

  <!-- Company names -->
  <g class="brand curabinix">
    <text class="brand-name" x="376" y="1832">CuraBinix</text>
  </g>
  <g class="brand tidy-pulp">
    <circle class="brand-dot" cx="1120" cy="1805" r="28"/>
    <text class="brand-name" x="1165" y="1820">Tidy Pulp</text>
  </g>
</svg>
</body>
</html>
```